Stationary pack for BrightNest

BrightNest is a recently establish Solar brokerage company based in Australia. We have a number of sales staff who provide advice and guidance to both residential and commercial customers regarding solar systems (solar hot water and solar panels.)

In addition to our brokerage services we are also developing software for the solar industry, which will be used to automate the solar system install process. This system will be used by other companies in the solar industry including installers, wholesalers and government departments.

We are after a stationary pack that consists of the following: Business cards, compliments slip and letter head.

The EPS, AI, PNG etc files for the logo are attached.

For the business card:
The name and logo of the company need to be clearly visible. On the back of the business cards, we would like the logo. I am happy for you to split the image part of the logo from the text if you think it would look better a different way.

I would like the business cards to be easily readable with the following information on the front:
Name
(Please leave room for titles for the future – eg Sales Advisor.)
Mobile
Office
Email
Address
ABN

Letter heads:
I would prefer the address to be at the top

Compliments slips:
Only need to be one sided

Target Market(s)

BrightNest provides services to both residential and commercial customers. Our customers will be environmentally conscious.

Industry/Entity Type

Residential

Requirements
Must have
• Business cards must have the logo on the back.

```html
<!DOCTYPE html>
<html lang="en">
<head>
<meta charset="utf-8">
<title>BrightNest Stationery Pack</title>
<link href="https://fonts.googleapis.com/css2?family=Nunito:wght@700;800&family=Merriweather:wght@400;700&display=swap" rel="stylesheet">
<style>
  :root {
    --green: #4ea83e;
    --green-deep: #2f8a2a;
    --green-pale: #d6ebc6;
    --blue: #235a8c;
    --sun: #f2c51c;
    --paper: #ffffff;
    --stage: #e6e7ea;
  }
  * { margin: 0; padding: 0; box-sizing: border-box; }
  html, body { width: 1134px; height: 1200px; overflow: hidden; }
  body { background: var(--stage); position: relative; font-family: "Nunito", sans-serif; }

  .sheet { position: absolute; background: var(--paper); overflow: hidden; }

  .brand { position: absolute; display: flex; align-items: center; gap: 8px; }
  .brand__dot { border-radius: 50%; background: var(--sun); flex: none; }
  .brand__name { font-family: "Nunito", sans-serif; font-weight: 800; color: var(--green); line-height: 1; }

  /* Letterhead */
  .letterhead { left: 307px; top: 122px; width: 631px; height: 891px; }
  .letterhead .brand { left: 14px; top: 100px; }
  .letterhead .brand__dot { width: 40px; height: 40px; }
  .letterhead .brand__name { font-size: 46px; }
  .letterhead__rule { position: absolute; left: 0; width: 100%; height: 4px; background: var(--green); }
  .letterhead__rule--one { top: 157px; }
  .letterhead__rule--two { top: 169px; }
  .letterhead__accent { position: absolute; left: 438px; top: 563px; width: 193px; height: 193px; border-radius: 50%;
    background: radial-gradient(circle, #fbe6a8 0 30%, #e6f1dc 31% 100%); opacity: .9; }
  .letterhead__footer { position: absolute; left: 0; bottom: 0; width: 100%; height: 190px; }

  /* Compliments slip */
  .slip { left: 145px; top: 314px; width: 690px; height: 330px; }
  .slip .brand { left: 17px; top: 78px; }
  .slip .brand__dot { width: 22px; height: 22px; }
  .slip .brand__name { font-size: 27px; }
  .slip__accent { position: absolute; left: 540px; top: 138px; width: 150px; height: 150px; border-radius: 50%;
    background: radial-gradient(circle, #fbe8b4 0 28%, #e9f2e0 29% 100%); }
  .slip__band { position: absolute; left: 0; bottom: 0; width: 100%; height: 40px;
    background: linear-gradient(90deg, #e9d63a 0%, #a6cf62 30%, #6cbd59 60%, #4fab42 100%);
    display: flex; align-items: center; justify-content: center; }
  .slip__message { font-family: "Merriweather", serif; font-weight: 700; font-size: 17px; color: var(--blue); letter-spacing: .2px; }

  /* Business card front */
  .card { width: 280px; height: 160px; }
  .card--front { left: 145px; top: 678px; }
  .card--front .brand { left: 10px; top: 30px; gap: 5px; }
  .card--front .brand__dot { width: 10px; height: 10px; }
  .card--front .brand__name { font-size: 13px; }
  .card__phones { position: absolute; right: 5px; top: 10px; font-size: 7.5px; color: var(--blue); text-align: right; line-height: 1.1; font-family: "Nunito", sans-serif; font-weight: 700; }
  .card__person { position: absolute; left: 0; top: 61px; width: 280px; text-align: center; padding-left: 0; }
  .card__name { font-size: 11px; font-weight: 800; color: var(--green); margin-left: 0; }
  .card__title { font-family: "Merriweather", serif; font-style: italic; font-size: 7px; color: var(--blue); }
  .card__accent { position: absolute; left: 218px; top: 70px; width: 62px; height: 62px; border-radius: 50%;
    background: radial-gradient(circle, #f8e6b6 0 30%, #eaf2e3 31% 100%); }
  .card__wave { position: absolute; left: 0; bottom: 0; width: 280px; height: 60px; }
  .card__web { position: absolute; left: 6px; bottom: 4px; font-family: "Merriweather", serif; font-size: 6.5px; color: var(--blue); line-height: 1.3; }
  .card__address { position: absolute; right: 36px; bottom: 3px; font-family: "Merriweather", serif; font-size: 8px; color: var(--green-deep); }

  /* Business card back */
  .card--back { left: 436px; top: 680px; }
  .card__surface { position: absolute; inset: 0; }
  .card--back .brand { left: 0; top: 0; width: 280px; height: 160px; flex-direction: column; justify-content: center; gap: 6px; padding-top: 6px; }
  .card--back .brand__dot { width: 26px; height: 26px; }
  .card--back .brand__name { font-size: 27px; }
</style>
</head>
<body>

  <section class="sheet letterhead" aria-label="Letterhead">
    <div class="brand"><span class="brand__dot"></span><span class="brand__name">BrightNest</span></div>
    <div class="letterhead__rule letterhead__rule--one"></div>
    <div class="letterhead__rule letterhead__rule--two"></div>
    <div class="letterhead__accent"></div>
    <svg class="letterhead__footer" viewBox="0 0 631 190" preserveAspectRatio="none">
      <defs>
        <linearGradient id="footerFill" x1="0" y1="0" x2="1" y2="1">
          <stop offset="0" stop-color="#7cc24e"/>
          <stop offset=".55" stop-color="#a9d67a"/>
          <stop offset="1" stop-color="#eef6e2"/>
        </linearGradient>
      </defs>
      <rect width="631" height="190" fill="url(#footerFill)" role="img" aria-label="Soft green grid texture background"/>
      <path d="M0 0 H631 V30 C480 110 200 110 0 40 Z" fill="#ffffff"/>
      <path d="M0 40 C200 110 480 110 631 30" fill="none" stroke="#2f8a2a" stroke-width="9"/>
      <path d="M0 52 C200 120 470 118 631 44" fill="none" stroke="#8fcf55" stroke-width="3" opacity=".8"/>
    </svg>
  </section>

  <section class="sheet slip" aria-label="Compliments slip">
    <div class="brand"><span class="brand__dot"></span><span class="brand__name">BrightNest</span></div>
    <div class="slip__accent"></div>
    <div class="slip__band"><p class="slip__message">Letter here can be typed in blue</p></div>
  </section>

  <section class="sheet card card--front" aria-label="Business card front">
    <div class="brand"><span class="brand__dot"></span><span class="brand__name">BrightNest</span></div>
    <p class="card__phones">office - +61 400 555 018<br>Mob - +61 400 555 018</p>
    <div class="card__person">
      <p class="card__name">Liam Carter</p>
      <p class="card__title">Sales Advisor</p>
    </div>
    <div class="card__accent"></div>
    <svg class="card__wave" viewBox="0 0 280 60" preserveAspectRatio="none">
      <defs>
        <linearGradient id="frontWave" x1="0" y1="0" x2="1" y2="0">
          <stop offset="0" stop-color="#f4f9ee"/>
          <stop offset="1" stop-color="#9fd16e"/>
        </linearGradient>
      </defs>
      <path d="M0 18 C90 50 200 42 280 10 V60 H0 Z" fill="url(#frontWave)" role="img" aria-label="Soft green grid texture"/>
      <path d="M0 18 C90 50 200 42 280 10" fill="none" stroke="#2f8a2a" stroke-width="4"/>
      <path d="M0 24 C90 54 200 47 280 16" fill="none" stroke="#8fcf55" stroke-width="1.5"/>
    </svg>
    <p class="card__web">www.brightnest.com.au<br>hello@brightnest.com.au</p>
    <p class="card__address">Address</p>
  </section>

  <section class="sheet card card--back" aria-label="Business card back">
    <svg class="card__surface" viewBox="0 0 280 160" preserveAspectRatio="none">
      <defs>
        <linearGradient id="backFill" x1="0" y1="0" x2="1" y2="1">
          <stop offset="0" stop-color="#6dbb45"/>
          <stop offset=".5" stop-color="#a8d67c"/>
          <stop offset="1" stop-color="#7cc24e"/>
        </linearGradient>
      </defs>
      <rect width="280" height="160" fill="url(#backFill)" role="img" aria-label="Soft green grid texture background"/>
      <path d="M0 42 C80 10 200 10 280 40 V125 C200 150 80 150 0 118 Z" fill="#ffffff"/>
      <path d="M0 42 C80 10 200 10 280 40" fill="none" stroke="#2f8a2a" stroke-width="4"/>
      <path d="M0 118 C80 150 200 150 280 125" fill="none" stroke="#2f8a2a" stroke-width="4"/>
    </svg>
    <div class="brand"><span class="brand__dot"></span><span class="brand__name">BrightNest</span></div>
  </section>

</body>
</html>
```